Web design for a pet services marketplace

I represent a South American based company: “TORVELIS” which provides a different array of pet related services. As a starting point, I would like to get proposals for 1 page website (plus a general frame for forms, instructions etc) web design job for a dog boarding marketplace. If you could add a logo is desirable.
By a Dog Boarding Marketplace, I mean a community marketplace, very much like an roomswap, but for pet services (initially dog boarding/daycare, but evolving to other services such as dog walkers. The purpose is to bring together dog owners and dog-care providers according to qualifications or characteristics given at time of input and needs of the dog owner given at the time of searching. Providers create a profile, entering certain information requested in forms such as their location, type of house/apt, what type/size of dogs they take, prior experience, as well as a personal introduction and pictures. Providers will set their own rates and calendar availability. Then customers browse, schedule and book and pay online. As it works for similar services, there will be a system of reviews and feedback for each care provider.
As to the website, it should be substantially similar to the following websites: (www.pupstayo.com , www.kelbo.com). It should be simple and straightforward, prioritizing ease of use. I would like for visitors to easily understand how the model works by seeing the home page, and getting pop up explanations by browsing over each main icon or message on the homepage. Therefore, I would try to keep additional pages to a minimum.
As I’m new to this, I would not venture as to how many pages I would need and would defer to your suggestion, according to the examples provided. However, I would like to have a visually striking front end, with dog related pictures or cartoon type images. Icons etc should be fun, and related to dogs, vacations, hotels/lodging, travel, etc. Secondary pages (like enrollment forms, Q&A, etc) could have a clean design, maybe adding some non-obtrusive related imagery.
Please note that attached pictures are , third party property and are for guide only.
Additional info:
In general I want to make a site very much like the examples of pupstayo and kelbo, but i think a better job could be done in terms of design. Please feel free to provide your own ideas.
1. For now, since the site will be new, we would not be including a testimonials section. However, we could use the space , or maybe smaller, with the "spread the love"section for announcing special deals for people who share the project.
2. In the principal section, I would like to see a clean layout. Much like pupstayo does. As an alternative, I would also like to see how it would look like if we handled more cartoon type drawings instead of pictures (just a suggestion to see how it would look like).
3. Search spaces should be more floating (merging more with background), as in pupstayo, not in larger boxes.
Updates
Please find in the attachments a very rough wire frame that i just did as response to a project proposal. Please note where i say OK (top and bottom) I mean that those two sections i found ok in such project or the model websites. Pretty regular content in those sections. Added Friday, July 10, 2015
Target Market(s)
dog owners, people who are willing to host pets in their home, kennels
Industry/Entity Type
Pet Care
Number of Pages Required
1 page
Look and feel

```html
<!DOCTYPE html>
<html lang="en">
<head>
<meta charset="utf-8">
<title>TORVELIS – Find a Loving Dog Sitter</title>
<link rel="stylesheet" href="https://fonts.googleapis.com/css2?family=Noto+Serif:wght@400;700&family=Arvo:wght@400;700&display=swap">
<style>
:root{
  --tan:#d6a47c;
  --tan-dark:#c98f63;
  --orange:#f26722;
  --peach:#fce6d7;
  --peach-line:#f6cdb2;
  --ink:#333333;
  --muted:#666666;
  --white:#ffffff;
  --serif:'Noto Serif', Georgia, serif;
  --slab:'Arvo', Georgia, serif;
}
*{box-sizing:border-box;margin:0;padding:0}
html,body{width:789px;height:1200px;overflow:hidden;background:var(--white)}
body{font-family:var(--serif);color:var(--ink);position:relative}

.top-bar{position:absolute;left:0;top:0;width:789px;height:54px;background:var(--tan)}
.top-nav{position:absolute;right:26px;top:19px;display:flex;gap:34px}
.top-nav a{color:var(--white);text-decoration:none;font-size:14px}
.brand{position:absolute;left:40px;top:0;width:140px;height:82px;background:var(--tan);border-radius:0 0 70px 70px;display:flex;align-items:center;justify-content:center;color:var(--white);font-size:16px;font-weight:700;letter-spacing:1px;padding-top:14px}

.hero-photo{position:absolute;left:26px;top:64px;width:370px;height:300px;border-radius:40px;background:radial-gradient(ellipse at 50% 55%,#c88a52 0%,#e0b383 40%,#f6e8dc 75%,#ffffff 100%)}
.hero-copy{position:absolute;left:395px;top:138px;width:370px;text-align:center}
.hero-title{font-size:32px;font-weight:400;color:var(--ink)}
.hero-sub{font-size:12px;color:var(--muted);margin-top:8px}
.search-row{position:absolute;left:423px;top:222px;display:flex;gap:8px}
.search-input{width:222px;height:36px;border:1px solid #ccc;border-radius:3px;display:flex;align-items:center;padding-left:10px;gap:8px;color:#999;font-size:13px}
.btn-orange{background:var(--orange);color:var(--white);border-radius:3px;font-size:13px;font-weight:700;display:flex;align-items:center;justify-content:center}
.search-btn{width:96px;height:36px}
.option-row{position:absolute;left:430px;top:267px;display:flex;gap:14px;align-items:center;font-size:11px;color:var(--orange)}
.date-btn{height:22px;padding:0 8px;font-size:9px;gap:4px}

.features-band{position:absolute;left:0;top:382px;width:789px;height:236px;background:var(--peach);border-top:1px solid var(--peach-line)}
.feature{position:absolute;top:20px;width:160px;text-align:center}
.feature-photo{width:134px;height:134px;border-radius:50%;margin:0 auto;border:5px solid var(--white);box-shadow:0 2px 4px rgba(0,0,0,.15)}
.feature-bone{position:relative;width:120px;height:46px;margin:18px auto 0}
.feature-bone svg{position:absolute;inset:0}
.feature-bone span{position:relative;display:block;line-height:46px;color:var(--white);font-family:var(--slab);font-size:19px;letter-spacing:1px}

.benefits{position:absolute;left:38px;top:644px;width:713px;height:158px;display:flex;border:1px solid #e6e6e6;background:var(--white)}
.benefit{flex:1;padding:26px 18px 0;text-align:center;border-right:1px solid #e6e6e6}
.benefit:last-child{border-right:0}
.benefit h3{font-size:18px;font-weight:400;margin-bottom:12px}
.benefit p{font-size:10px;line-height:1.35;color:var(--ink)}

.spread{position:absolute;left:0;top:818px;width:789px;height:196px}
.spread-copy{position:absolute;left:40px;top:22px;width:390px;text-align:center}
.spread-copy h2{font-size:32px;font-weight:400}
.spread-copy p{font-size:13px;margin-top:10px;line-height:1.4}
.share-btn{width:124px;height:36px;margin:14px auto 0}
.spread-photo{position:absolute;left:524px;top:0;width:240px;height:190px;border-radius:30px;background:radial-gradient(ellipse at 50% 50%,#c9874f 0%,#e8c7a8 40%,#d9344a 62%,#ffffff 85%)}

.footer{position:absolute;left:0;top:1014px;width:789px;height:186px;background:var(--tan);color:var(--white)}
.footer-col{position:absolute;top:22px}
.footer-col h4{font-size:14px;font-weight:700;margin-bottom:6px}
.footer-col li{list-style:none;font-size:9.5px;line-height:1.3}
.newsletter{position:absolute;left:490px;top:22px;width:270px}
.newsletter h4{font-size:14px;font-weight:700;margin-bottom:10px}
.email-row{display:flex}
.email-input{width:220px;height:28px;background:var(--white);color:#888;font-size:12px;padding-left:8px;display:flex;align-items:center}
.go-btn{width:46px;height:28px;font-size:11px;border-radius:0}
.store-row{display:flex;gap:24px;margin:24px 0 0 18px}
.store-badge{width:90px;height:30px;background:#111;border-radius:5px}
.copyright{position:absolute;left:555px;top:168px;font-size:8px}
</style>
</head>
<body>

<header class="top-bar">
  <div class="brand">TORVELIS</div>
  <nav class="top-nav"><a href="#">Log In</a><a href="#">Sign Up</a></nav>
</header>

<section class="hero">
  <div class="hero-photo" role="img" aria-label="Two fluffy puppies lying together with a teddy bear"></div>
  <div class="hero-copy">
    <h1 class="hero-title">Find a Loving Dog Sitter</h1>
    <p class="hero-sub">Search thousands of trusted, insured pet sitters near you.</p>
  </div>
  <div class="search-row">
    <div class="search-input">
      <svg width="12" height="16" viewBox="0 0 12 16"><path d="M6 0a6 6 0 0 1 6 6c0 4-6 10-6 10S0 10 0 6a6 6 0 0 1 6-6z" fill="#f26722"/><circle cx="6" cy="6" r="2.2" fill="#fff"/></svg>
      City or Zip
    </div>
    <div class="btn-orange search-btn">Find a Sitter</div>
  </div>
  <div class="option-row">
    <span>◉ Overnight</span>
    <span>◯ Daycare</span>
    <span class="btn-orange date-btn">
      <svg width="9" height="9" viewBox="0 0 9 9"><rect x="0.5" y="1.5" width="8" height="7" fill="none" stroke="#fff"/><line x1="0.5" y1="3.5" x2="8.5" y2="3.5" stroke="#fff"/></svg>Start Date</span>
    <span class="btn-orange date-btn">
      <svg width="9" height="9" viewBox="0 0 9 9"><rect x="0.5" y="1.5" width="8" height="7" fill="none" stroke="#fff"/><line x1="0.5" y1="3.5" x2="8.5" y2="3.5" stroke="#fff"/></svg>End Date</span>
  </div>
</section>

<section class="features-band">
  <div class="feature" style="left:38px">
    <div class="feature-photo" style="background:radial-gradient(circle,#8a6a52,#d9cfc6)" role="img" aria-label="A group of dogs sitting together"></div>
    <div class="feature-bone">
      <svg viewBox="0 0 120 46" width="120" height="46"><g fill="var(--tan)"><circle cx="12" cy="12" r="11"/><circle cx="12" cy="34" r="11"/><circle cx="108" cy="12" r="11"/><circle cx="108" cy="34" r="11"/><rect x="10" y="8" width="100" height="30" rx="4"/></g></svg>
      <span>Search</span>
    </div>
  </div>
  <div class="feature" style="left:315px">
    <div class="feature-photo" style="background:radial-gradient(circle,#d0873a,#f3e6d8)" role="img" aria-label="A small dog beside a packed suitcase"></div>
    <div class="feature-bone">
      <svg viewBox="0 0 120 46" width="120" height="46"><g fill="var(--tan)"><circle cx="12" cy="12" r="11"/><circle cx="12" cy="34" r="11"/><circle cx="108" cy="12" r="11"/><circle cx="108" cy="34" r="11"/><rect x="10" y="8" width="100" height="30" rx="4"/></g></svg>
      <span>Book</span>
    </div>
  </div>
  <div class="feature" style="left:591px">
    <div class="feature-photo" style="background:radial-gradient(circle,#3a3330,#a59a92)" role="img" aria-label="A dog relaxing on a bed"></div>
    <div class="feature-bone">
      <svg viewBox="0 0 120 46" width="120" height="46"><g fill="var(--tan)"><circle cx="12" cy="12" r="11"/><circle cx="12" cy="34" r="11"/><circle cx="108" cy="12" r="11"/><circle cx="108" cy="34" r="11"/><rect x="10" y="8" width="100" height="30" rx="4"/></g></svg>
      <span>Relax</span>
    </div>
  </div>
</section>

<section class="benefits">
  <div class="benefit">
    <h3>Insured Pets</h3>
    <p>Lorem ipsum dolor sit amet, consectetur adipiscing elit. In dapibus est et tempus scelerisque</p>
  </div>
  <div class="benefit">
    <h3>Vetted Hosts</h3>
    <p>Lorem ipsum dolor sit amet, consectetur adipiscing elit. In dapibus est et tempus scelerisque</p>
  </div>
  <div class="benefit">
    <h3>One on One TLC</h3>
    <p>Lorem ipsum dolor sit amet, consectetur adipiscing elit. In dapibus est et tempus scelerisque</p>
  </div>
</section>

<section class="spread">
  <div class="spread-copy">
    <h2>Spread the Love</h2>
    <p>Tell a friend about TORVELIS, and they’ll<br>get $10 off their first reservation.</p>
    <div class="btn-orange share-btn">Start Sharing</div>
  </div>
  <div class="spread-photo" role="img" aria-label="A fluffy puppy holding a red heart"></div>
</section>

<footer class="footer">
  <div class="footer-col" style="left:44px">
    <h4>Company</h4>
    <ul><li>About Us</li><li>Mobile</li><li>Press</li><li>Blog</li><li>Customer Reviews</li><li>Our Investors</li><li>Jobs</li><li>Terms of Service</li><li>Privacy Policy</li></ul>
  </div>
  <div class="footer-col" style="left:190px">
    <h4>Help</h4>
    <ul><li>Support Center</li><li>How it Works</li><li>Contact Us</li><li>Coverage</li></ul>
  </div>
  <div class="footer-col" style="left:322px">
    <h4>Hosting</h4>
    <ul><li>Become a Sitter</li><li>How Hosting Works</li><li>Hosting Tips</li><li>Hosting Policy</li></ul>
  </div>
  <div class="newsletter">
    <h4>Keep me updated</h4>
    <div class="email-row">
      <div class="email-input">Enter your email</div>
      <div class="btn-orange go-btn">GO</div>
    </div>
    <div class="store-row">
      <div class="store-badge" role="img" aria-label="App store download badge"></div>
      <div class="store-badge" role="img" aria-label="App store download badge"></div>
    </div>
  </div>
  <p class="copyright">© TORVELIS 2015</p>
</footer>

</body>
</html>
```